Pagecraft Design Project - Vibrant Children's school bag website

We need a fresh design for the landing page of our new web site and blog: quillonmarket.com

Tamborine specialises in supplying schools all over the world and now also parents directly with, personalised school bags, accessories, crafts and gifts for their children.

I have attached the visual that our web designers have provided so that we can see the layout of the various window, but now we need to add the personal touch of making it our own and visually making the site look enticing and exciting to shop on.
Updates

Hello Designers,

We are now in the final round of choosing a design.  We have found that most deisgns are very similar and that none are completley original.  Therefore, we are willing to throw our wire frame away and start with a compleltely new visual so you can design what ever you like!

The only requirements we have is that we must have:
- A large rolling banner to show our products lines
- Our Company logo
- Meta going tags across the top
- Icons for chatterbook,snipboard,blog,
- Account Login bar
- A log in area for schools
- A login area to register for the Club Tambo

So we are looking for something that really stands out from the crowd!

can you deliver?

Thanks,

Target Market(s)

To appeal to mum's shopping on line for their children's school items and gifts.

Industry/Entity Type

School

Requirements
Must have
• -When you see the visual attached please note the amendments:
- the word 'school bags' under our company name will not appear
- the tag line "Australia's no 1 specialist school bag company' should be deleted. We will leave this area open so that you can include some simple icons that we would like featured across the top of the banner i.e:
- a love heart icon + wording to say : Made with love
- A 'delivery' icon + wording to say : Free delivery
- A 'warranty' icon + wording to say : up to 25 year warranty
- A 'world' icon + wording to say : we ship to the universe
(Please see: www.pebblecrate.com.au for reference of what we mean!)

We we want the overall design to be clean, fresh, crisp and fun to look at.

You may alter the colours of everything, even the coloured tabs. we think that the coloured tabs should actually just be one colour through out and to let the tamborine name stand out with all it's.

The top/main photo will be a rolling banner.

You can change the shapes of the boxes but keep to the wire frame.

Please alter the design of the black/coloured club tambo card to suit your design.

Our aim is to also change the side panels in peak seasons to reflect halloween banner, christmas banner etc.

Please see my screen shot of the current page and see where the "dots' pattern sits on either side of the shopping panels. Please include the side panels as we want to change the design to have themes i.e for halloween, for christmas etc etc.

example of websites that have this:

http://www.wavemoorly.com/

Please include a 'blog' and snipboard icon.

The site will not only manage our retail sales but will also be a portal for our schools to register and place their bulk orders with us. So the "wholesale register box" must stand out so our school customers can easily see where they need to click & register.
Should not have
• Please do not do a 'baby' boutique theme. We need a theme that appeals to mum's that have children across the ages of 3-14 years.

```html
<!DOCTYPE html>
<html lang="en">
<head>
<meta charset="utf-8">
<title>Tamborine – Kids School Bags</title>
<link rel="stylesheet" href="https://fonts.googleapis.com/css2?family=Ubuntu:wght@300;400;500&family=Comfortaa:wght@400;700&display=swap">
<style>
:root{
  --bar:#555456;
  --page:#f1f1f1;
  --white:#ffffff;
  --line:#dcdcdc;
  --text:#555;
  --muted:#999;
  --link:#1aa3d8;
  --teal:#2bb6c9;
  --red:#c8102e;
  --btn:#a0001e;
  --brand:#e4407b;
}
*{box-sizing:border-box;margin:0;padding:0}
html,body{width:1200px;height:1191px;overflow:hidden}
body{position:relative;background:var(--page);font-family:"Ubuntu",sans-serif;color:var(--text)}
.abs{position:absolute}
.topbar{left:0;top:0;width:1200px;height:33px;background:var(--bar);color:#ddd;font:300 10px "Comfortaa",sans-serif}
.topbar .mail{left:191px;top:11px}
.topbar .links{right:215px;top:11px;display:flex;gap:18px}
.topbar .links span::before{content:"→ ";color:#999}
.logo{left:203px;top:56px;font:700 40px "Comfortaa",sans-serif;color:var(--brand);letter-spacing:-1px;white-space:nowrap}
.logo sup{font-size:8px;letter-spacing:0}
.perk{top:64px;display:flex;align-items:center;gap:6px;font:300 10px/9px "Ubuntu",sans-serif;color:#8a6a6a}
.perk svg{flex:none}
.country{left:899px;top:76px;font-size:10px;color:var(--muted)}
.country u{margin-left:8px}
.search{left:847px;top:103px;width:147px;height:16px;background:var(--white);border:1px solid #e8e8e8;font-size:9px;color:#aaa;padding:2px 6px}
.search-go{left:1002px;top:103px;width:15px;height:15px;border-radius:50%;background:#ccc}
.nav{left:180px;top:127px;width:840px;height:38px;background:#f4f4f4;border:1px solid var(--line);display:flex;align-items:center;padding-left:16px;gap:23px;font-size:10px;color:#8b7070;text-transform:uppercase}
.nav .on{color:var(--link)}
.hero{left:181px;top:165px;width:618px;height:354px;background:radial-gradient(circle at 30% 45%,#e8c8a0 0 18%,transparent 35%),linear-gradient(90deg,#9b5a28,#e3a418 45%,#f2c217 70%,#6a4d12)}
.dots{left:711px;top:499px;display:flex;gap:4px}
.dots i{width:11px;height:11px;border-radius:50%;background:#fff}
.dots i:first-child{background:#1aa3d8}
.side{left:799px;width:220px;background:var(--white);text-align:center}
.side .pic{width:100%}
.side h3{font:400 12px "Ubuntu",sans-serif;color:#444;margin-top:3px}
.side p{font-size:11px;color:var(--muted)}
.strip{left:180px;top:531px;width:840px;height:30px;background:repeating-linear-gradient(45deg,#f7f7f7 0 3px,#efefef 3px 6px);border:1px solid #e6e6e6;font:400 13px "Comfortaa",sans-serif;color:var(--teal);padding:7px 0 0 62px;white-space:nowrap}
.strip svg{position:absolute;left:23px;top:5px}
.promo{top:572px;height:96px;background:var(--white);padding:4px;width:274px}
.promo div{height:100%;color:#fff;font:300 27px/29px "Ubuntu",sans-serif;padding:18px 0 0 30px;display:flex;justify-content:space-between;align-items:flex-start;overflow:hidden}
.promo .label{white-space:nowrap}
.promo .icon{flex:none;width:56px;height:50px;margin:2px 28px 0 0;border-radius:8px;background:rgba(255,255,255,.35)}
.panel-left{left:26px;top:690px;width:127px;height:31px;background:#ececec}
.latest{left:197px;top:687px;font:400 19px "Ubuntu",sans-serif;color:#444;letter-spacing:-1px}
.products{left:181px;top:714px;width:838px;height:216px;background:var(--white);border:1px solid var(--line)}
.card{top:8px;width:197px;height:200px}
.card .pic{height:127px;border:1px solid #ddd;box-shadow:0 1px 2px rgba(0,0,0,.1);display:flex;align-items:center;justify-content:center}
.card .pic span{width:110px;height:100px;border-radius:8px}
.card h4{font:400 12px "Ubuntu",sans-serif;color:var(--red);margin:14px 0 0 9px;white-space:nowrap}
.card .price{position:absolute;left:11px;top:176px;font-size:12px;color:#333}
.card .add{position:absolute;right:6px;top:167px;width:79px;height:25px;background:var(--btn);color:#fff;font-size:10px;text-align:center;line-height:25px}
.quote{left:180px;top:947px;width:840px;height:61px;border-top:1px solid #e4e4e4;border-bottom:1px solid #e4e4e4}
.quote b{position:absolute;left:5px;top:4px;font:700 50px Georgia,serif;color:#ccc}
.quote p{position:absolute;left:60px;top:10px;width:760px;font:400 14px/16px "Comfortaa",sans-serif;color:#888}
.col{top:1025px;font-size:11px}
.col h5{font:400 12px "Ubuntu",sans-serif;color:#333;margin-bottom:24px}
.col li{list-style:none;font:300 9.5px "Comfortaa",sans-serif;color:#aaa;height:19px}
.footer{left:0;top:1157px;width:1200px;height:34px;background:var(--bar);color:#bbb;font:300 10px "Comfortaa",sans-serif}
.footer .copy{left:181px;top:12px}
.footer .links{right:180px;top:12px;display:flex;gap:17px}
</style>
</head>
<body>
<header>
  <div class="abs topbar">
    <span class="abs mail">Join our mailing list to receive great deals</span>
    <div class="abs links"><span>My Account</span><span>Login/Register</span><span>Your Basket</span></div>
  </div>
  <div class="abs logo">tamborine<sup>TM</sup></div>
  <div class="abs perk" style="left:454px"><svg width="34" height="30" viewBox="0 0 34 30"><path d="M17 29C4 19 1 13 1 8a8 8 0 0 1 16-2 8 8 0 0 1 16 2c0 5-3 11-16 21z" fill="#d01e2a"/></svg><span>Made<br>with<br>love</span></div>
  <div class="abs perk" style="left:551px"><svg width="36" height="28" viewBox="0 0 36 28"><rect x="1" y="4" width="21" height="16" fill="#7a8aa0"/><path d="M22 9h8l5 6v5H22z" fill="#3a66b0"/><circle cx="8" cy="22" r="4" fill="#333"/><circle cx="28" cy="22" r="4" fill="#333"/></svg><span>Free<br>Delivery</span></div>
  <div class="abs perk" style="left:649px"><svg width="32" height="32"><circle cx="16" cy="16" r="15" fill="#e2b53c"/><circle cx="16" cy="16" r="11" fill="#f4d77a"/></svg><span>Upto<br>25 years<br>warranty</span></div>
  <div class="abs perk" style="left:747px"><svg width="32" height="32"><circle cx="16" cy="16" r="15" fill="#3a7fc4"/><path d="M6 12c5-4 9 2 13-1s6 4 8 8" stroke="#8fc46a" stroke-width="4" fill="none"/></svg><span>We ship<br>to the<br>universe</span></div>
  <div class="abs country">Change Country <u>USA</u> ▼</div>
  <div class="abs search">Search Product</div>
  <div class="abs search-go"></div>
  <nav class="abs nav"><span class="on">Home</span><span>Kids Backpacks</span><span>Kids Bags</span><span>Sports</span><span>Kids Clothing</span><span>Art &amp; Craft</span><span>Music</span><span>Kids Diaries</span><span>Kids Storage</span><span>Extra Stuff</span><span>Sale</span></nav>
</header>

<main>
  <div class="abs hero" role="img" aria-label="Rolling banner photo: smiling girl wearing a pink school backpack against a golden autumn background"></div>
  <div class="abs dots"><i></i><i></i><i></i><i></i><i></i></div>

  <div class="abs side" style="top:165px;height:186px">
    <div class="pic" role="img" aria-label="Three kids backpacks in floral, pink and orange" style="height:142px;background:linear-gradient(90deg,#777 0 30%,#e8dfe4 30% 62%,#f08a30 62%)"></div>
    <h3>KIDS BAG</h3><p>Starting from $25</p>
  </div>
  <div class="abs side" style="top:351px;height:168px;background:transparent">
    <div class="pic" style="height:132px;background:#ececec;display:flex;justify-content:center;align-items:center"><span role="img" aria-label="Colourful kids home reading diary cover" style="width:83px;height:120px;background:linear-gradient(#f5d62a,#5cae3a 70%,#f5d62a)"></span></div>
    <div style="background:#fff;height:36px;padding-top:1px"><h3>KIDS DIARY</h3><p>Starting from $20</p></div>
  </div>

  <div class="abs strip"><svg width="22" height="22"><circle cx="11" cy="11" r="9.5" fill="#fff" stroke="#666" stroke-width="1.5"/><path d="M11 5v6h-4" stroke="#666" stroke-width="1.5" fill="none"/></svg>Did you know that we are shipping 24/7 worldwide and free of charge? See what else we've got to offer!</div>

  <div class="abs promo" style="left:180px"><div style="background:linear-gradient(120deg,#c93a6e,#e66c9c)"><span class="label">&nbsp;24 / 7<br>Support</span><span class="icon"></span></div></div>
  <div class="abs promo" style="left:461px"><div style="background:linear-gradient(120deg,#8db82a,#b2d44e)"><span class="label">&nbsp;Free<br>Shipping</span><span class="icon"></span></div></div>
  <div class="abs promo" style="left:743px"><div style="background:linear-gradient(120deg,#2fb3cf,#5ed0e4);padding-left:26px"><span class="label">&nbsp;15%<sup style="font-size:11px">Off</sup><br>Club Tambo</span><span class="icon" style="background:#222;transform:rotate(-25deg);width:50px;height:44px;margin-right:22px;margin-top:6px"></span></div></div>

  <div class="abs panel-left"></div>
  <h2 class="abs latest">LATEST PRODUCTS</h2>
  <section class="abs products">
    <div class="abs card" style="left:8px"><div class="pic"><span role="img" aria-label="Navy school backpack" style="background:#2d3a78;width:90px"></span></div><h4>Ergo Sturdy Packs™</h4><div class="price">$ 59.95</div><div class="add">Add to cart</div></div>
    <div class="abs card" style="left:216px"><div class="pic"><span role="img" aria-label="Green insulated lunch box with food" style="background:#8fc44a;width:160px"></span></div><h4>Colourfull Lunch Box</h4><div class="price">$ 24.95</div><div class="add">Add to cart</div></div>
    <div class="abs card" style="left:424px"><div class="pic"><span role="img" aria-label="Blue sports duffel bag" style="background:#2f4aa8;width:170px;height:75px"></span></div><h4>Sports Bag</h4><div class="price">$ 59.95</div><div class="add">Add to cart</div></div>
    <div class="abs card" style="left:633px"><div class="pic"><span role="img" aria-label="Stack of colourful reusable shopping bags" style="background:linear-gradient(#d6336e,#f0852a,#3a7fc4)"></span></div><h4>Enviro Shopping Bags</h4><div class="price">$ 9.95</div><div class="add">Add to cart</div></div>
  </section>

  <blockquote class="abs quote"><b>“</b><p>Lorem Ipsum est simplement du faux texte employé dans la compositi on et la mise en page avant impression.</p></blockquote>

  <div class="abs col" style="left:239px"><h5>Categories</h5><ul><li>Accessories</li><li>Clothing</li><li>Electronics</li><li>Sale</li></ul></div>
  <div class="abs col" style="left:434px"><h5>Brands</h5><ul><li>StoreDune</li><li>StoreCanyon</li><li>StoreRiver</li><li>StoreForest</li></ul></div>
  <div class="abs col" style="left:654px"><h5>Colours</h5><ul><li>White</li><li>Red</li><li>Blue</li><li>Black</li></ul></div>
  <div class="abs col" style="left:841px"><h5>Price Range</h5><ul><li>$10 - $ 20</li><li>$30 - $ 40</li><li>$50 - $ 60</li><li>$70 - $ 80</li></ul></div>
</main>

<footer class="abs footer">
  <span class="abs copy">Copyright Tamborine . All Right Reserved</span>
  <div class="abs links"><span>Homepage</span><span>Shop</span><span>Terms &amp; Conditions</span><span>Blog</span><span>Contact Us</span></div>
</footer>
</body>
</html>
```